Brightgate Business Card Design

Name Marisa Okonduye
Title Mortgage Originator
Office (800) 555-0142 x65
Direct (240) 555-0187
Email mokonduye@brightgatehomes.example
NMLS 5830472
Licensed MD

Name Deron Plummer
Title Mortgage Originator
Office (800) 555-0142 x66
Direct (404) 555-0163
Email dplummer@brightgatehomes.example
NMLS 5917360
Licensed MD

Name Lakendra Burton
Title Mortgage Originator
Office (800) 555-0142 x67
Direct (443) 555-0129
Email burtonlakendra@mailbox.example
NMLS 5372619
Licensed MD

Name Samir Qudwaheli
Title Mortgage Originator
Office (800) 555-0142 x32
Direct (571) 555-0176
Email squdwaheli@brightgatehomes.example
NMLS 4068259
Licensed MD

```html
<!DOCTYPE html>
<html lang="en">
<head>
<meta charset="utf-8">
<title>Brightgate Business Cards</title>
<link href="https://fonts.googleapis.com/css2?family=Libre+Baskerville:wght@400;700&family=Barlow:wght@400&display=swap" rel="stylesheet">
<style>
:root{
  --backdrop:#96979b;
  --card:#ffffff;
  --navy:#0f2340;
  --gold:#c9a24a;
  --gold-light:#e6cf8c;
  --ink:#2a2a2a;
}
*{box-sizing:border-box;margin:0;padding:0}
html,body{width:1200px;height:1200px;overflow:hidden;background:var(--backdrop)}
.sheet{position:relative;width:1200px;height:1200px}
.card{position:absolute;width:382px;height:218px;background:var(--card);border-radius:12px;overflow:hidden}
.card--a{left:196px;top:360px}
.card--b{left:622px;top:360px}
.card--c{left:196px;top:622px}
.card--d{left:622px;top:622px}
.card__art{position:absolute;inset:0;width:382px;height:218px}
.brand{position:absolute;left:21px;top:16px;display:flex;align-items:center;gap:6px;
  font-family:"Libre Baskerville",serif;font-weight:700;font-size:17px;color:var(--navy)}
.brand__mark{width:10px;height:10px;background:var(--navy)}
.name{position:absolute;left:21px;top:60px;max-width:188px;font-family:"Libre Baskerville",serif;font-weight:700;
  font-size:18.5px;letter-spacing:-0.5px;color:var(--navy);white-space:nowrap}
.title{position:absolute;left:23px;top:89px;font-family:"Libre Baskerville",serif;font-weight:700;
  font-size:10.5px;letter-spacing:0.3px;color:var(--gold);white-space:nowrap}
.contacts{position:absolute;left:21px;top:114px;list-style:none;font-family:"Barlow",sans-serif;
  font-size:12.5px;color:var(--ink);line-height:16.4px}
.contacts li{display:flex;align-items:center;gap:6px;height:16.4px;white-space:nowrap}
.contacts .icon{width:14px;height:14px;flex:none}
.contacts .spacer{width:14px;flex:none}
.contacts .email{font-size:9.4px;letter-spacing:-0.1px}
</style>
</head>
<body>
<div class="sheet">

<svg width="0" height="0" style="position:absolute">
  <defs>
    <symbol id="icon-phone" viewBox="0 0 14 14"><circle cx="7" cy="7" r="6" fill="none" stroke="#c9a24a" stroke-width="1"/><path d="M4.6 4.2l1.3-.3.7 1.5-.8.6c.4.9 1 1.5 1.9 1.9l.6-.8 1.5.7-.3 1.3c-2.6 0-4.9-2.3-4.9-4.9z" fill="#c9a24a"/></symbol>
    <symbol id="icon-mail" viewBox="0 0 14 14"><circle cx="7" cy="7" r="6" fill="none" stroke="#c9a24a" stroke-width="1"/><rect x="4" y="5" width="6" height="4.2" rx=".5" fill="#c9a24a"/><path d="M4 5.3l3 2 3-2" fill="none" stroke="#fff" stroke-width=".7"/></symbol>
    <symbol id="icon-pin" viewBox="0 0 14 14"><circle cx="7" cy="7" r="6" fill="none" stroke="#c9a24a" stroke-width="1"/><path d="M7 10.5c-1.6-1.8-2.4-3.1-2.4-4.1a2.4 2.4 0 0 1 4.8 0c0 1-.8 2.3-2.4 4.1z" fill="none" stroke="#c9a24a" stroke-width=".9"/><circle cx="7" cy="6.4" r=".8" fill="#c9a24a"/></symbol>
    <linearGradient id="gold-sheen" x1="0" y1="0" x2="0" y2="1">
      <stop offset="0" stop-color="#b8913a"/><stop offset=".5" stop-color="#f1dc9c"/><stop offset="1" stop-color="#b8913a"/>
    </linearGradient>
    <linearGradient id="tone-a" x1="0" y1="0" x2="1" y2="1"><stop offset="0" stop-color="#8a7766"/><stop offset=".5" stop-color="#4a3428"/><stop offset="1" stop-color="#6b5a3a"/></linearGradient>
    <linearGradient id="tone-b" x1="0" y1="0" x2="1" y2="1"><stop offset="0" stop-color="#2a2a2e"/><stop offset=".55" stop-color="#3c2c26"/><stop offset="1" stop-color="#1f2740"/></linearGradient>
    <linearGradient id="tone-c" x1="0" y1="0" x2="1" y2="1"><stop offset="0" stop-color="#f2efec"/><stop offset=".5" stop-color="#8a5a3c"/><stop offset="1" stop-color="#e9c7b2"/></linearGradient>
    <linearGradient id="tone-d" x1="0" y1="0" x2="1" y2="1"><stop offset="0" stop-color="#e4e2df"/><stop offset=".5" stop-color="#6e5446"/><stop offset="1" stop-color="#b9bcaa"/></linearGradient>
  </defs>
</svg>

<article class="card card--a">
  <svg class="card__art" viewBox="0 0 382 218">
    <path d="M250 12 A155 155 0 0 0 222 150" fill="none" stroke="url(#gold-sheen)" stroke-width="1.6"/>
    <circle cx="376" cy="128" r="150" fill="var(--navy)"/>
    <circle cx="357" cy="109" r="140" fill="url(#gold-sheen)"/>
    <circle cx="364" cy="109" r="136" fill="#fff"/>
    <circle cx="367" cy="109" r="133" fill="url(#tone-a)" role="img" aria-label="Portrait photo of Marisa Okonduye"/>
  </svg>
  <div class="brand"><span class="brand__mark"></span>Brightgate</div>
  <h2 class="name">Marisa Okonduye</h2>
  <p class="title">MORTGAGE ORIGINATOR</p>
  <ul class="contacts">
    <li><svg class="icon"><use href="#icon-phone"/></svg>(800) 555-0142 x65</li>
    <li><svg class="icon"><use href="#icon-phone"/></svg>(240) 555-0187</li>
    <li><svg class="icon"><use href="#icon-mail"/></svg><span class="email">mokonduye@brightgatehomes.example</span></li>
    <li><svg class="icon"><use href="#icon-pin"/></svg>NMLS 5830472</li>
    <li><span class="spacer"></span>Licensed MD</li>
  </ul>
</article>

<article class="card card--b">
  <svg class="card__art" viewBox="0 0 382 218">
    <path d="M250 12 A155 155 0 0 0 222 150" fill="none" stroke="url(#gold-sheen)" stroke-width="1.6"/>
    <circle cx="376" cy="128" r="150" fill="var(--navy)"/>
    <circle cx="357" cy="109" r="140" fill="url(#gold-sheen)"/>
    <circle cx="364" cy="109" r="136" fill="#fff"/>
    <circle cx="367" cy="109" r="133" fill="url(#tone-b)" role="img" aria-label="Portrait photo of Deron Plummer"/>
  </svg>
  <div class="brand"><span class="brand__mark"></span>Brightgate</div>
  <h2 class="name">Deron Plummer</h2>
  <p class="title">MORTGAGE ORIGINATOR</p>
  <ul class="contacts">
    <li><svg class="icon"><use href="#icon-phone"/></svg>(800) 555-0142 x66</li>
    <li><svg class="icon"><use href="#icon-phone"/></svg>(404) 555-0163</li>
    <li><svg class="icon"><use href="#icon-mail"/></svg><span class="email">dplummer@brightgatehomes.example</span></li>
    <li><svg class="icon"><use href="#icon-pin"/></svg>NMLS 5917360</li>
    <li><span class="spacer"></span>Licensed MD</li>
  </ul>
</article>

<article class="card card--c">
  <svg class="card__art" viewBox="0 0 382 218">
    <path d="M250 12 A155 155 0 0 0 222 150" fill="none" stroke="url(#gold-sheen)" stroke-width="1.6"/>
    <circle cx="376" cy="128" r="150" fill="var(--navy)"/>
    <circle cx="357" cy="109" r="140" fill="url(#gold-sheen)"/>
    <circle cx="364" cy="109" r="136" fill="#fff"/>
    <circle cx="367" cy="109" r="133" fill="url(#tone-c)" role="img" aria-label="Portrait photo of Lakendra Burton"/>
  </svg>
  <div class="brand"><span class="brand__mark"></span>Brightgate</div>
  <h2 class="name">Lakendra Burton</h2>
  <p class="title">MORTGAGE ORIGINATOR</p>
  <ul class="contacts">
    <li><svg class="icon"><use href="#icon-phone"/></svg>(800) 555-0142 x67</li>
    <li><svg class="icon"><use href="#icon-phone"/></svg>(443) 555-0129</li>
    <li><svg class="icon"><use href="#icon-mail"/></svg><span class="email">burtonlakendra@mailbox.example</span></li>
    <li><svg class="icon"><use href="#icon-pin"/></svg>NMLS 5372619</li>
    <li><span class="spacer"></span>Licensed MD</li>
  </ul>
</article>

<article class="card card--d">
  <svg class="card__art" viewBox="0 0 382 218">
    <path d="M250 12 A155 155 0 0 0 222 150" fill="none" stroke="url(#gold-sheen)" stroke-width="1.6"/>
    <circle cx="376" cy="128" r="150" fill="var(--navy)"/>
    <circle cx="357" cy="109" r="140" fill="url(#gold-sheen)"/>
    <circle cx="364" cy="109" r="136" fill="#fff"/>
    <circle cx="367" cy="109" r="133" fill="url(#tone-d)" role="img" aria-label="Portrait photo of Samir Qudwaheli"/>
  </svg>
  <div class="brand"><span class="brand__mark"></span>Brightgate</div>
  <h2 class="name">Samir Qudwaheli</h2>
  <p class="title">MORTGAGE ORIGINATOR</p>
  <ul class="contacts">
    <li><svg class="icon"><use href="#icon-phone"/></svg>(800) 555-0142 x32</li>
    <li><svg class="icon"><use href="#icon-phone"/></svg>(571) 555-0176</li>
    <li><svg class="icon"><use href="#icon-mail"/></svg><span class="email">squdwaheli@brightgatehomes.example</span></li>
    <li><svg class="icon"><use href="#icon-pin"/></svg>NMLS 4068259</li>
    <li><span class="spacer"></span>Licensed MD</li>
  </ul>
</article>

</div>
</body>
</html>
```